New Website for Belcourt Manor at www.belcourt.com.au

A new logo has been designed (through pixel forge) and we now want to align the look and feel of our website at www.belcourt.com.au to the new logo. The content and page names (e.g. Grounds) will remain largely unchanged for the new site, so please submit a new look "Home" page, using our new logo, current text and any photos you choose from the existing gallery at our website. I have also attached the current "Home" page photos.

Industry/Entity Type

Accommodation

Number of Pages Required

1 page

Requirements
Must have
• Logo to be presented on white background.

```html
<!DOCTYPE html>
<html lang="en">
<head>
<meta charset="utf-8">
<title>Belcourt Manor – Home</title>
<link rel="stylesheet" href="https://fonts.googleapis.com/css2?family=Open+Sans:ital,wght@0,400;0,600;0,700;1,400&family=Great+Vibes&display=swap">
<style>
  :root {
    --link: #1a86cc;
    --text: #3a3a3a;
    --heading: #2b2b2b;
    --band: rgba(60, 60, 60, 0.55);
    --white: #ffffff;
    --brand: #1a7fc4;
  }
  * { box-sizing: border-box; margin: 0; padding: 0; }
  html, body {
    width: 1200px; height: 842px; overflow: hidden;
    background: var(--white);
    font-family: "Open Sans", Arial, sans-serif;
    color: var(--text);
  }
  .page { position: relative; width: 1200px; height: 842px; }

  .hero {
    position: absolute; left: 0; top: 0; width: 1200px; height: 539px;
    background: linear-gradient(180deg,
      #2f4a2c 0%, #3f6336 14%, #c9552e 24%, #e0683a 33%,
      #e7c55a 45%, #e3c45c 62%, #b9b3a8 78%, #8f8a82 100%);
  }
  .hero-band {
    position: absolute; left: 0; top: 488px; width: 1200px; height: 51px;
    background: var(--band);
    display: flex; align-items: center; justify-content: flex-end;
    padding-right: 82px; gap: 28px;
  }
  .hero-tagline {
    font-family: "Great Vibes", cursive;
    font-size: 33px; color: var(--white); letter-spacing: 0.3px;
  }
  .hero-button {
    display: inline-flex; align-items: center; gap: 10px;
    height: 23px; padding: 0 8px 0 9px;
    background: linear-gradient(#ffffff, #e4e4e4);
    border: 1px solid #cfcfcf; border-radius: 2px;
    font-size: 8.5px; font-weight: 700; color: #333; text-decoration: none;
  }

  .main-nav {
    position: absolute; left: 0; top: 551px; width: 1200px;
    text-align: center; font-size: 12.6px;
  }
  .main-nav a { color: var(--link); text-decoration: none; }
  .main-nav .sep { color: #999; margin: 0 4px; }

  .brand {
    position: absolute; left: 83px; top: 622px;
    display: flex; align-items: center; gap: 12px;
  }
  .brand-dot { width: 22px; height: 22px; border-radius: 50%; background: var(--brand); }
  .brand-name { font-size: 29px; font-weight: 600; color: var(--brand); }

  .intro {
    position: absolute; left: 434px; top: 595px; width: 420px;
    font-size: 12.3px; line-height: 15px;
  }
  .intro p { margin-bottom: 14px; }
  .intro a { color: var(--link); font-style: italic; text-decoration: none; }

  .address {
    position: absolute; left: 913px; top: 598px; width: 200px;
    text-align: center; font-size: 12.3px; font-weight: 700;
    line-height: 14.5px; color: var(--heading);
  }
  .address svg { display: block; margin: 0 auto 24px; }
</style>
</head>
<body>
<div class="page">
  <header class="hero" role="img" aria-label="Aerial photograph of the yellow manor house with terracotta tiled roofs, arched walkway and gravel drive, surrounded by palms and green trees">
    <div class="hero-band">
      <span class="hero-tagline">Palatial Estate and Luxury Resort</span>
      <a class="hero-button" href="#">Browse Gallery
        <svg width="6" height="8" viewBox="0 0 6 8"><path d="M1 1l3 3-3 3" fill="none" stroke="#1a86cc" stroke-width="1.4"/></svg>
      </a>
    </div>
  </header>

  <nav class="main-nav">
    <a href="#">Main</a><span class="sep">|</span><a href="#">Mansion</a><span class="sep">|</span><a href="#">Bedrooms</a><span class="sep">|</span><a href="#">Options</a><span class="sep">|</span><a href="#">Fox and Hound</a><span class="sep">|</span><a href="#">Grounds</a><span class="sep">|</span><a href="#">Location</a><span class="sep">|</span><a href="#">Gallery</a><span class="sep">|</span><a href="#">Contact</a><span class="sep">|</span><a href="#">Availability</a><span class="sep">|</span><a href="#">DIY Weddings</a>
  </nav>

  <div class="brand">
    <span class="brand-dot"></span>
    <span class="brand-name">Belcourt Manor</span>
  </div>

  <section class="intro">
    <p>On over 2 manicured garden acres, Belcourt Manor is a unique Gold Coast estate, centrally located in the prestigious rural suburb of Wendale.<br><a href="#">More about our Location</a></p>
    <p>The estate features a grand mansion, private pub (The Fox and Hound), sparkling resort pool, tennis court and playground.</p>
    <p>Magnificent properties rarely feel so warm and welcoming – so browse away and visit <a href="#">our photo gallery</a> – and we look forward to having you stay as our guests.</p>
    <p>For prices, availability and guest reviews, visit <a href="#">StayNest</a></p>
  </section>

  <address class="address">
    <svg width="22" height="32" viewBox="0 0 22 32" aria-hidden="true">
      <path d="M11 0C4.9 0 0 4.9 0 11c0 8 11 21 11 21s11-13 11-21C22 4.9 17.1 0 11 0z" fill="#1a86cc"/>
      <circle cx="11" cy="11" r="4" fill="#fff"/>
    </svg>
    19 Belcourt Drive<br>Wendale, Gold Coast<br>Queensland, Australia
  </address>
</div>
</body>
</html>
```